Sunny Paths and joy Business card

I have a logo, but will like a business card design. Is for a travel agency in Mexico. We focus in family experiences.

I will liek some thing different and unique, from the traditional business card, something to get remmeber for.

Business card information:

Leandro T. Ocampo
leandro@sunnypathsjoy.example

Alameda 482, 3 piso
Col. Tlalpizco
Mexico, D.F. 07320

office: (55) 5000-0142
mobile: (55) 9000-0187

www.sunnypathsjoy.example
@sunnypjoy
blog: sunnypathsandjoy.blogsite.example
facebook: SunnyPathsAndJoy

```html
<!DOCTYPE html>
<html lang="es">
<head>
<meta charset="utf-8">
<title>Sunny Paths and joy – Business Card</title>
<link rel="stylesheet" href="https://fonts.googleapis.com/css2?family=Nunito:wght@400;800&display=swap">
<style>
  :root {
    --sky-deep: #0b6ebe;
    --sky-light: #3fb6ec;
    --sky-pale: #86cff2;
    --sky-edge: #1b86d3;
    --cloud: #ffffff;
    --ink-blue: #1a6cbd;
    --brand-blue: #1c5cae;
    --white: #ffffff;
  }
  * { margin: 0; padding: 0; box-sizing: border-box; }
  html, body { width: 1200px; height: 667px; overflow: hidden; background: #ffffff; }
  .card {
    position: relative;
    width: 1200px;
    height: 667px;
    overflow: hidden;
    font-family: "Nunito", "Helvetica Neue", Arial, sans-serif;
  }
  .card-sky { position: absolute; inset: 0; }
  .cloud-glow { fill: none; stroke: var(--sky-pale); stroke-width: 44; stroke-linejoin: round; }
  .cloud-edge { fill: none; stroke: var(--sky-edge); stroke-width: 20; stroke-linejoin: round; }
  .cloud-fill { fill: var(--cloud); stroke: none; }
  .holder { position: absolute; left: 410px; top: 26px; color: var(--white); }
  .holder-name { font-weight: 800; font-size: 29px; letter-spacing: 0.3px; line-height: 1.3; }
  .holder-email { font-weight: 400; font-size: 31px; line-height: 1.35; }
  .contact-list {
    position: absolute; left: 410px; top: 228px;
    list-style: none; color: var(--ink-blue);
    font-size: 31px; line-height: 44px; font-weight: 400;
    white-space: nowrap;
  }
  .brand { position: absolute; left: 28px; top: 215px; width: 300px; }
  .brand-art {
    display: block; margin-left: 105px; width: 195px; height: 125px;
    border-radius: 60px 60px 40px 40px;
    background: radial-gradient(circle at 45% 45%, #2e6fcf 0%, #5f9be0 45%, #cfe6f7 100%);
  }
  .brand-name {
    margin-top: 6px; color: var(--brand-blue);
    font-weight: 800; font-size: 33px; line-height: 36px; text-align: center;
  }
  .address {
    position: absolute; left: 410px; top: 566px;
    color: var(--white); font-style: normal;
    font-size: 31px; line-height: 44px;
  }
</style>
</head>
<body>
<main class="card">
  <svg class="card-sky" width="1200" height="667" viewBox="0 0 1200 667" aria-hidden="true">
    <defs>
      <linearGradient id="lower-sky" x1="0" y1="0" x2="1" y2="1">
        <stop offset="0" stop-color="#63c3ee"/>
        <stop offset="1" stop-color="#19aee9"/>
      </linearGradient>
      <path id="cloud-shape" d="M -20 200 A 70 50 0 0 1 110 175 A 80 55 0 0 1 260 165 A 110 60 0 0 1 470 160 A 100 55 0 0 1 660 165 A 90 50 0 0 1 830 175 A 80 55 0 0 1 980 165 A 70 50 0 0 1 1110 185 A 70 50 0 0 1 1220 190 L 1220 470 A 90 50 0 0 1 1060 480 A 110 55 0 0 1 860 490 A 100 50 0 0 1 680 500 A 120 55 0 0 1 460 505 A 110 50 0 0 1 250 490 A 100 50 0 0 1 60 470 A 60 40 0 0 1 -20 460 Z"/>
    </defs>
    <rect width="1200" height="667" fill="url(#lower-sky)"/>
    <rect width="1200" height="320" fill="var(--sky-deep)"/>
    <g class="cloud-band">
      <use href="#cloud-shape" class="cloud-glow"/>
      <use href="#cloud-shape" class="cloud-edge"/>
      <use href="#cloud-shape" class="cloud-fill"/>
    </g>
  </svg>

  <header class="holder">
    <p class="holder-name">LEANDRO T. OCAMPO</p>
    <p class="holder-email">leandro@sunnypathsjoy.example</p>
  </header>

  <div class="brand">
    <span class="brand-art" role="img" aria-label="Illustration of a cheerful blue airplane carrying a family, the agency's mascot"></span>
    <p class="brand-name">Sunny Paths<br>and joy</p>
  </div>

  <ul class="contact-list">
    <li>office: (55) 5000-0142 • mobile: (55) 9000-0187</li>
    <li>www.sunnypathsjoy.example</li>
    <li>@sunnypjoy</li>
    <li>blog: sunnypathsandjoy.blogsite.example</li>
    <li>facebook: SunnyPathsAndJoy</li>
  </ul>

  <address class="address">
    Alameda 482, 3 piso, Col. Tlalpizco<br>
    Mexico, D.F. 07320
  </address>
</main>
</body>
</html>
```